Creation of a book cover
Size : 14 x 20,5 cm (+ 5 mm bleed area at the top, bottom and right areas)
The Title is a French sentence which means “The heron dreaming on the cold roof of this empty station”. It’s a surrealistic title which has no link to the story.
AUTHOR : Mathieu Vorlange
TITLE : "Le héron rêvant sur le toit froid de cette gare vide »
PUBLISHER (AT THE BOTTOM OF THE PAGE) : Editions Parvenche
I send a PDF file with the kind of cover we have imagine, but you can propose something different. The glass and the fly can of course be used.

```html
<!DOCTYPE html>
<html lang="fr">
<head>
<meta charset="utf-8">
<title>Le héron rêvant sur le toit froid de cette gare vide — Mathieu Vorlange</title>
<link href="https://fonts.googleapis.com/css2?family=Bebas+Neue&family=Oswald:wght@500&family=PT+Sans+Narrow:wght@700&display=swap" rel="stylesheet">
<style>
  :root {
    --page-bg: #dedede;
    --cover-top: #9ccac3;
    --cover-mid: #6c9fb2;
    --cover-low: #bcd6d8;
    --table-light: #eef3ee;
    --table-warm: #f3f1c6;
    --author-red: #b3262a;
    --title-white: #f7f7f5;
    --title-shadow: rgba(40, 70, 85, 0.55);
    --publisher-green: #1f5846;
    --art-dark: #6f8f98;
    --art-light: #c9dfe0;
  }
  html, body {
    margin: 0;
    padding: 0;
    width: 1200px;
    height: 900px;
    overflow: hidden;
    background: var(--page-bg);
  }
  .canvas {
    position: relative;
    width: 1200px;
    height: 900px;
  }
  .book-cover {
    position: absolute;
    left: 320px;
    top: 55px;
    width: 560px;
    height: 790px;
    overflow: hidden;
    background:
      radial-gradient(ellipse 70% 40% at 50% 18%, rgba(210, 236, 226, 0.75), rgba(210, 236, 226, 0) 70%),
      linear-gradient(180deg, var(--cover-top) 0%, #86b7b8 30%, var(--cover-mid) 52%, #8db6c0 68%, var(--cover-low) 100%);
  }
  .table-surface {
    position: absolute;
    left: 0;
    right: 0;
    top: 615px;
    bottom: 0;
    background: linear-gradient(100deg, var(--table-light) 0%, #eef3ea 55%, var(--table-warm) 100%);
  }
  .author {
    position: absolute;
    top: 86px;
    left: 0;
    right: 0;
    text-align: center;
    margin: 0;
  }
  .author-name {
    display: inline-block;
    font-family: "Oswald", sans-serif;
    font-weight: 500;
    font-size: 27px;
    letter-spacing: 0.5px;
    color: var(--author-red);
    font-variant: small-caps;
    padding: 0 4px 4px;
    border-bottom: 1.5px solid var(--author-red);
  }
  .title {
    position: absolute;
    left: 46px;
    top: 218px;
    margin: 0;
    font-family: "Bebas Neue", sans-serif;
    font-weight: 400;
    color: var(--title-white);
    text-shadow: 3px 4px 0 rgba(160, 180, 185, 0.9), 8px 12px 14px var(--title-shadow);
    line-height: 0.95;
  }
  .title-line { display: block; }
  .title-line--first { font-size: 74px; }
  .title-line--second { font-size: 74px; padding-left: 2px; }
  .title-line--third { font-size: 52px; padding-left: 14px; }
  .title-line--third .title-accent { font-size: 72px; }
  .cover-art {
    position: absolute;
    left: 24px;
    top: 448px;
    width: 320px;
    height: 342px;
    border-radius: 6px 6px 0 0;
    background: linear-gradient(180deg, var(--art-light) 0%, #a9c8cc 45%, var(--art-dark) 100%);
    opacity: 0.85;
  }
  .publisher {
    position: absolute;
    right: 46px;
    top: 724px;
    margin: 0;
    font-family: "PT Sans Narrow", sans-serif;
    font-weight: 700;
    font-size: 25px;
    color: var(--publisher-green);
  }
</style>
</head>
<body>
<div class="canvas">
  <section class="book-cover">
    <div class="table-surface"></div>
    <p class="author"><span class="author-name">Mathieu Vorlange</span></p>
    <h1 class="title">
      <span class="title-line title-line--first">Le héron rêvant</span>
      <span class="title-line title-line--second">sur le toit froid</span>
      <span class="title-line title-line--third">de cette <span class="title-accent">gare vide</span></span>
    </h1>
    <div class="cover-art" role="img" aria-label="Illustration of a fly perched on the rim of a glass of water with rising bubbles"></div>
    <p class="publisher">Éditions Parvenche</p>
  </section>
</div>
</body>
</html>
```